Business Card Design

We sell fish products to corporate food companies who then turn these products into final food products for consumers

Industry/Entity Type

Business

Contact Information for Business Card

I need a corporate business card template for a fish products business. We would like it be professional for use in dealing with multi national companies. This company business card template will be used by multiple employees so the following fields must be open to edit (Name, Phone Number and Email address)

```html
<!DOCTYPE html>
<html lang="en">
<head>
<meta charset="utf-8">
<title>Tidewell Seafoods – Business Card</title>
<link href="https://fonts.googleapis.com/css2?family=Didact+Gothic&family=Questrial&family=Open+Sans:wght@700&display=swap" rel="stylesheet">
<style>
  :root {
    --page-bg: #e4e4e4;
    --card-white: #ffffff;
    --brand-navy: #1457a8;
    --wave-dark: #1a5fb4;
    --wave-light: #3fa0dc;
    --wave-pale: #7cc3ec;
    --accent-green: #62b987;
    --text-on-blue: #ffffff;
  }
  html, body {
    margin: 0;
    padding: 0;
    width: 1200px;
    height: 750px;
    overflow: hidden;
    background: var(--page-bg);
  }
  .canvas {
    position: relative;
    width: 1200px;
    height: 750px;
  }
  .business-card {
    position: absolute;
    left: 50px;
    top: 61px;
    width: 1100px;
    height: 628px;
    border-radius: 44px;
    overflow: hidden;
    background: var(--card-white);
    box-shadow: 0 6px 18px rgba(0,0,0,0.18);
  }
  .wave-art {
    position: absolute;
    inset: 0;
  }
  .brand {
    position: absolute;
    right: 80px;
    top: 92px;
    display: flex;
    align-items: center;
    gap: 16px;
    font-family: "Questrial", sans-serif;
    font-size: 46px;
    letter-spacing: 2px;
    color: var(--brand-navy);
  }
  .brand-dot {
    width: 34px;
    height: 34px;
    border-radius: 50%;
    background: var(--brand-navy);
  }
  .holder {
    position: absolute;
    right: 62px;
    top: 238px;
    color: var(--text-on-blue);
    font-family: "Open Sans", sans-serif;
    font-weight: 700;
    font-size: 27px;
  }
  .holder .role {
    font-family: "Questrial", sans-serif;
    font-weight: 400;
    font-size: 23px;
  }
  .contact {
    position: absolute;
    left: 72px;
    bottom: 44px;
    margin: 0;
    padding: 0;
    list-style: none;
    color: var(--text-on-blue);
    font-family: "Didact Gothic", sans-serif;
    font-size: 26px;
    line-height: 32px;
  }
  .contact li {
    display: flex;
    align-items: center;
    gap: 8px;
  }
  .contact .icon {
    width: 20px;
    height: 20px;
    flex: none;
  }
</style>
</head>
<body>
<div class="canvas">
  <div class="business-card">
    <svg class="wave-art" viewBox="0 0 1100 628" width="1100" height="628" aria-hidden="true">
      <defs>
        <linearGradient id="waveFill" x1="0" y1="0" x2="0.4" y2="1">
          <stop offset="0" stop-color="var(--wave-pale)"/>
          <stop offset="0.45" stop-color="var(--wave-light)"/>
          <stop offset="1" stop-color="#2b8fd3"/>
        </linearGradient>
      </defs>
      <path fill="var(--accent-green)" d="M0,352 C300,366 480,318 640,236 C800,154 950,132 1100,122 L1100,628 L0,628 Z"/>
      <path fill="var(--card-white)" d="M0,358 C300,372 480,324 640,242 C800,160 950,138 1100,128 L1100,628 L0,628 Z"/>
      <path fill="var(--wave-dark)" d="M0,368 C300,382 480,334 640,252 C800,170 950,148 1100,138 L1100,628 L0,628 Z"/>
      <path fill="url(#waveFill)" d="M0,384 C300,398 500,350 660,270 C810,194 950,166 1100,158 L1100,628 L0,628 Z"/>
    </svg>

    <div class="brand">
      <span class="brand-dot"></span>
      <span class="brand-name">TIDEWELL SEAFOODS</span>
    </div>

    <div class="holder">Alex Morgan <span class="role">/Manager</span></div>

    <ul class="contact">
      <li>14 Harbour Lane</li>
      <li>Portside VIC 3999</li>
      <li>
        <svg class="icon" viewBox="0 0 20 20" aria-hidden="true"><path fill="#fff" d="M5 2l3 4-2 2c1 3 3 5 6 6l2-2 4 3-2 3C9 18 2 11 2 4z"/></svg>
        + 999 999 9999
      </li>
      <li>
        <svg class="icon" viewBox="0 0 20 20" aria-hidden="true"><rect x="2" y="5" width="16" height="11" fill="#fff"/><path d="M2 5l8 6 8-6" fill="none" stroke="#3fa0dc" stroke-width="1.6"/></svg>
        info@tidewell.com
      </li>
    </ul>
  </div>
</div>
</body>
</html>
```